Harbourlight Campus Lodgings needs a business card design

Hi Guys,

We are a Student Accommodation company in Australia. We already have a logo which I will submit.

I will require the design of the business cards from you.

I am after something that looks clean, modern and that people feel interested and actually want to contact us.

We would like to see designs that are innovative.

On the business cards I will require to have:

Employee Name
Position
Phone number
Email
Facebook page

I hope you can help me with this project guys as I have heard really good things from you.

```html
<!DOCTYPE html>
<html lang="en">
<head>
<meta charset="utf-8">
<title>Harbourlight Campus Lodgings – Business Card</title>
<link rel="stylesheet" href="https://fonts.googleapis.com/css2?family=Arimo:wght@400;700&display=swap">
<style>
  :root {
    --green: #178f3a;
    --yellow: #fbbd2e;
    --white: #ffffff;
    --backdrop: #8f8f8f;
    --ink-green: #1a8f3c;
  }
  * { margin: 0; padding: 0; box-sizing: border-box; }
  html, body { width: 1200px; height: 725px; overflow: hidden; }
  body {
    background: var(--backdrop);
    font-family: "Arimo", Arial, sans-serif;
    display: flex;
    align-items: center;
    justify-content: center;
    gap: 26px;
  }
  .card {
    position: relative;
    width: 560px;
    height: 320px;
    overflow: hidden;
    box-shadow: 0 6px 18px rgba(0,0,0,0.25);
  }
  .card-front { background: var(--white); }
  .card-back { background: var(--green); }
  .card-bands { position: absolute; inset: 0; }

  .brand {
    position: absolute;
    display: flex;
    align-items: center;
    gap: 14px;
  }
  .brand-mark { width: 58px; height: 58px; background: var(--yellow); flex: none; }
  .brand-name {
    font-weight: 700;
    font-size: 22px;
    line-height: 1.08;
    text-transform: uppercase;
    letter-spacing: 0.5px;
  }
  .card-front .brand { left: 40px; top: 100px; }
  .card-front .brand-name { color: var(--ink-green); }
  .card-back .brand { left: 50%; top: 50%; transform: translate(-50%, -62%); }
  .card-back .brand-mark { width: 66px; height: 66px; }
  .card-back .brand-name { color: var(--yellow); font-size: 25px; }

  .contact { position: absolute; left: 300px; top: 64px; }
  .employee-name { color: var(--ink-green); font-weight: 700; font-size: 22px; }
  .employee-position { color: var(--yellow); font-weight: 700; font-size: 16px; margin-top: 2px; }
  .contact-list { list-style: none; margin-top: 16px; }
  .contact-item {
    display: flex;
    align-items: center;
    gap: 10px;
    color: var(--ink-green);
    font-size: 15px;
    height: 30px;
  }
  .contact-icon { width: 20px; height: 20px; flex: none; }
</style>
</head>
<body>

  <section class="card card-front" aria-label="Business card front">
    <svg class="card-bands" viewBox="0 0 560 320" aria-hidden="true">
      <rect x="0" y="0" width="560" height="18" fill="var(--yellow)"/>
      <polygon points="0,258 372,258 342,298 0,298" fill="var(--green)"/>
      <polygon points="360,320 392,276 560,276 560,320" fill="var(--yellow)"/>
    </svg>

    <div class="brand">
      <span class="brand-mark" aria-hidden="true"></span>
      <p class="brand-name">Harbourlight<br>Campus<br>Lodgings</p>
    </div>

    <div class="contact">
      <h1 class="employee-name">Employee Name</h1>
      <p class="employee-position">Position</p>
      <ul class="contact-list">
        <li class="contact-item">
          <svg class="contact-icon" viewBox="0 0 20 20" aria-hidden="true">
            <circle cx="10" cy="10" r="8.5" fill="none" stroke="var(--yellow)" stroke-width="1.6"/>
            <path d="M7 5.5 L8.6 5.5 L9.2 8 L8.2 8.8 C8.8 10.2 9.8 11.2 11.2 11.8 L12 10.8 L14.5 11.4 L14.5 13 C14.5 13.6 14 14 13.4 14 C9.6 13.7 6.3 10.4 6 6.6 C6 6 6.4 5.5 7 5.5 Z" fill="var(--yellow)"/>
          </svg>
          <span>1234 567 890</span>
        </li>
        <li class="contact-item">
          <svg class="contact-icon" viewBox="0 0 20 20" aria-hidden="true">
            <rect x="2" y="5" width="16" height="11" fill="var(--yellow)"/>
            <polyline points="2,5 10,11 18,5" fill="none" stroke="var(--white)" stroke-width="1.4"/>
          </svg>
          <span>@harbourlightlodgings.com</span>
        </li>
        <li class="contact-item">
          <svg class="contact-icon" viewBox="0 0 20 20" aria-hidden="true">
            <rect x="2.5" y="2.5" width="15" height="15" fill="none" stroke="var(--yellow)" stroke-width="1.6"/>
          </svg>
          <span>harbourlightlodgings</span>
        </li>
      </ul>
    </div>
  </section>

  <section class="card card-back" aria-label="Business card back">
    <svg class="card-bands" viewBox="0 0 560 320" aria-hidden="true">
      <rect x="0" y="272" width="560" height="48" fill="var(--yellow)"/>
      <polygon points="322,320 340,272 354,272 336,320" fill="var(--green)"/>
    </svg>

    <div class="brand">
      <span class="brand-mark" aria-hidden="true"></span>
      <p class="brand-name">Harbourlight<br>Campus<br>Lodgings</p>
    </div>
  </section>

</body>
</html>
```